Swimming Pool Business Billboard

10' x 24' Billboard displaying company name, logo and phone number. Picture of swimming pool activity; kids playing , swimming, etc. Bullet points possibly shown: New Construction, Repairs, Weekly maintenance.

Industry/Entity Type

Swimming pool construction, repairs and maintenance.

Font styles to use
Sans Serif

Colors
0054AA
0677BA
7BADD7
CADEEF
E8F1F8

Requirements
Must have
• Rusty & Calder Pembrook, RUSTY'S POOLS & Service,
Nice to have
• Prefer to have my last name "Pembrook" above the word "POOLS" only in smaller print so that "RUSTYS POOLS" is distinguished.

```html
<!DOCTYPE html>
<html lang="en">
<head>
<meta charset="utf-8">
<title>Rusty's Pools &amp; Service Billboard</title>
<link rel="stylesheet" href="https://fonts.googleapis.com/css2?family=Alfa+Slab+One&family=Source+Serif+4:opsz,wght@8..60,600&family=Oswald:wght@600&family=Montserrat:wght@700&display=swap">
<style>
  :root {
    --navy: #1b3562;
    --navy-deep: #142a50;
    --sky: #a8cbe5;
    --mist: #e8f1f8;
    --white: #ffffff;
    --page: #dcdcdc;
    --water: #4fb3e0;
    --deck: #c9b49a;
  }
  html, body {
    margin: 0;
    width: 954px;
    height: 1200px;
    overflow: hidden;
    background: var(--page);
  }
  .billboard {
    position: absolute;
    left: 27px;
    top: 412px;
    width: 900px;
    height: 375px;
    box-shadow: 0 3px 8px rgba(0,0,0,0.25);
    background: var(--white);
  }
  .billboard svg { display: block; }
  .owners { font-family: "Source Serif 4", Georgia, serif; font-weight: 600; fill: var(--navy); }
  .brand-slab { font-family: "Alfa Slab One", Georgia, serif; fill: var(--navy); }
  .brand-serif { font-family: "Source Serif 4", Georgia, serif; font-weight: 600; fill: var(--navy); }
  .service-label { font-family: "Oswald", "Arial Narrow", sans-serif; font-weight: 600; fill: var(--white); }
  .contact { font-family: "Montserrat", Arial, sans-serif; font-weight: 700; fill: var(--white); }
  .logo-name { font-family: "Montserrat", Arial, sans-serif; font-weight: 700; fill: var(--navy); }
</style>
</head>
<body>
<div class="billboard">
  <svg width="900" height="375" viewBox="0 0 900 375" xmlns="http://www.w3.org/2000/svg">
    <defs>
      <linearGradient id="poolPhoto" x1="0" y1="0" x2="0.4" y2="1">
        <stop offset="0" stop-color="#5d6b3e"/>
        <stop offset="0.18" stop-color="#d9cfbf"/>
        <stop offset="0.3" stop-color="#2f9fd8"/>
        <stop offset="0.65" stop-color="#8fd3ef"/>
        <stop offset="0.85" stop-color="#e8e2d6"/>
        <stop offset="1" stop-color="var(--deck)"/>
      </linearGradient>
      <radialGradient id="badgeFill" cx="0.4" cy="0.35" r="0.7">
        <stop offset="0" stop-color="#2a4a80"/>
        <stop offset="1" stop-color="var(--navy-deep)"/>
      </radialGradient>
    </defs>

    <!-- pool photo area -->
    <path class="pool-photo" role="img" aria-label="Photo of children splashing and playing in a backyard swimming pool"
          d="M582 0 L900 0 L900 258 C820 272 720 296 640 292 C604 290 612 210 620 150 C628 90 608 35 582 0 Z"
          fill="url(#poolPhoto)"/>
    <path d="M582 0 C600 25 615 45 612 70" fill="none" stroke="var(--sky)" stroke-width="10"/>

    <!-- waves -->
    <path class="wave-light" d="M0 318 C150 270 330 282 520 290 C680 296 800 270 900 248 L900 275 C780 300 650 316 480 312 C300 308 150 310 0 345 Z" fill="var(--sky)"/>
    <path class="wave-navy" d="M0 340 C160 305 330 300 520 306 C700 312 800 296 900 270 L900 375 L0 375 Z" fill="var(--navy)"/>

    <!-- logo placeholder -->
    <g class="logo">
      <circle cx="112" cy="112" r="58" fill="var(--navy)"/>
      <text class="logo-name" x="112" y="205" font-size="17" text-anchor="middle">RUSTY'S POOLS</text>
    </g>

    <!-- title block -->
    <text class="owners" x="201" y="46" font-size="28" textLength="324" lengthAdjust="spacingAndGlyphs">Rusty &amp; Calder Pembrook</text>
    <text class="brand-slab" x="200" y="113" font-size="62" textLength="326" lengthAdjust="spacingAndGlyphs">RUSTY'S</text>
    <text class="brand-slab" x="246" y="171" font-size="62" textLength="233" lengthAdjust="spacingAndGlyphs">POOLS</text>
    <text class="brand-serif" x="210" y="234" font-size="72" textLength="307" lengthAdjust="spacingAndGlyphs">&amp; Service</text>

    <!-- service badges -->
    <g class="badge">
      <circle cx="599" cy="61" r="49" fill="var(--sky)"/>
      <circle cx="599" cy="61" r="43" fill="url(#badgeFill)"/>
      <text class="service-label" x="599" y="57" font-size="15" text-anchor="middle">New</text>
      <text class="service-label" x="599" y="74" font-size="15" text-anchor="middle">Construction</text>
    </g>
    <g class="badge">
      <circle cx="572" cy="163" r="49" fill="var(--sky)"/>
      <circle cx="572" cy="163" r="43" fill="url(#badgeFill)"/>
      <text class="service-label" x="572" y="169" font-size="16" text-anchor="middle">Repairs</text>
    </g>
    <g class="badge">
      <circle cx="566" cy="267" r="49" fill="var(--sky)"/>
      <circle cx="566" cy="267" r="43" fill="url(#badgeFill)"/>
      <text class="service-label" x="566" y="263" font-size="15" text-anchor="middle">Weekly</text>
      <text class="service-label" x="566" y="280" font-size="15" text-anchor="middle">Maintenance</text>
    </g>

    <!-- contact row -->
    <g class="icon-phone" fill="none" stroke="var(--white)" stroke-width="2.2" stroke-linecap="round">
      <path d="M66 332 c-3 4 4 15 10 17 c2 1 4 0 5 -2 l-3 -4 l-3 1 c-2 -1 -4 -4 -4 -6 l2 -2 l-3 -4 z" fill="var(--white)" stroke="none"/>
      <path d="M77 331 a6 6 0 0 1 5 5"/>
      <path d="M78 326 a11 11 0 0 1 9 9"/>
    </g>
    <text class="contact" x="128" y="349" font-size="21" textLength="120" lengthAdjust="spacingAndGlyphs">912-555-0147</text>

    <g class="icon-mail" fill="none" stroke="var(--white)" stroke-width="1.6">
      <rect x="265" y="333" width="22" height="15"/>
      <polyline points="265,333 276,343 287,333"/>
    </g>
    <text class="contact" x="297" y="347" font-size="16" textLength="187" lengthAdjust="spacingAndGlyphs">rusty@rcpools.net</text>

    <g class="icon-pin">
      <path d="M508 330 a7 7 0 0 1 7 7 c0 5 -7 13 -7 13 c0 0 -7 -8 -7 -13 a7 7 0 0 1 7 -7 z" fill="var(--white)"/>
      <circle cx="508" cy="337" r="2.6" fill="var(--navy)"/>
    </g>
    <text class="contact" x="521" y="347" font-size="16" textLength="331" lengthAdjust="spacingAndGlyphs">2750 Marlow Creek Rd Brantley, GA 31599</text>
  </svg>
</div>
</body>
</html>
```